New home maintenance business, on the back of business card i would like dot points of my services provided.
these include,
General household repairs and maintenance
Painting
Verolin/Plaster Repairs
Fencing
Gardening and landscaping
Cleaning and removals
Doors and windows
Hinges and Locks
Fly screen/ screen door Repairs
I like black,silver, red but ill leav it up to you guys as something may be better for business.. , would also it be possible to create a logo for me incorporating the K&T as i want to make up t shirts in future thankyou
i would also like to put Marco Vintelli on the cards aswell please, and on back change painter to proffesional painter and decorator, please
i like alot of the designs sofar, i cant put my finger on wat 1 yet though!! cheers guys
Business
K&T HOME MAINTENANCE SERVICES
Lewis Vintelli 0467205184
kntmaintenance@postvale.com
ABN:57140328619

```html
<!DOCTYPE html>
<html lang="en">
<head>
<meta charset="utf-8">
<title>K&amp;T Home Maintenance Services – Business Card</title>
<link href="https://fonts.googleapis.com/css2?family=Questrial&family=Mulish:ital,wght@0,700;1,700&display=swap" rel="stylesheet">
<style>
  :root {
    --page-bg: #e9e6e1;
    --card-black: #141414;
    --card-charcoal: #3a3a3a;
    --silver: #b9b9b9;
    --silver-light: #d6d6d6;
    --silver-dim: #8a8a8a;
  }
  * { margin: 0; padding: 0; box-sizing: border-box; }
  html, body {
    width: 1200px; height: 900px; overflow: hidden;
    background: var(--page-bg);
    font-family: "Questrial", "Century Gothic", sans-serif;
  }
  .sheet {
    width: 1200px; height: 900px;
    display: flex; flex-direction: column;
    align-items: center; justify-content: center; gap: 40px;
  }
  .card {
    position: relative;
    width: 640px; height: 390px;
    border-radius: 4px;
    overflow: hidden;
    box-shadow: 0 10px 28px rgba(0,0,0,.28);
    color: var(--silver);
  }
  .card--front {
    background:
      radial-gradient(ellipse 60% 70% at 62% 30%, rgba(120,120,120,.55), transparent 70%),
      linear-gradient(160deg, var(--card-charcoal) 0%, #242424 45%, var(--card-black) 100%);
  }
  .card--back {
    background: linear-gradient(170deg, #262626 0%, var(--card-black) 100%);
  }
  .stripe-accent {
    position: absolute;
    width: 150px; height: 130px;
    background: linear-gradient(90deg, transparent, rgba(170,170,170,.22) 50%, transparent);
    -webkit-mask-image: linear-gradient(180deg, transparent, #000 40%, #000 60%, transparent);
            mask-image: linear-gradient(180deg, transparent, #000 40%, #000 60%, transparent);
  }
  .card--front .stripe-accent { left: 40px; top: 190px; }
  .card--back .stripe-accent { right: 70px; top: 210px; }

  .brand-name {
    position: absolute; left: 26px; top: 22px;
    font-size: 46px; letter-spacing: -1px;
    color: var(--silver-light);
  }
  .contact-person {
    position: absolute; right: 44px; top: 112px;
    text-align: left; width: 190px;
  }
  .contact-person__name {
    font-family: "Mulish", sans-serif; font-weight: 700;
    font-size: 22px; color: var(--silver);
  }
  .contact-person__phone {
    font-size: 22px; letter-spacing: 1px;
    padding-bottom: 6px;
    border-bottom: 3px solid var(--silver-dim);
  }
  .business-title {
    position: absolute; left: 40px; top: 200px;
    font-size: 31px; letter-spacing: -0.5px;
    color: var(--silver-light);
    white-space: nowrap;
  }
  .business-details {
    position: absolute; left: 210px; top: 285px;
    font-size: 21px; line-height: 1.35;
  }

  .services {
    position: absolute; left: 34px; top: 26px;
  }
  .services__heading {
    font-family: "Mulish", sans-serif; font-weight: 700; font-style: italic;
    font-size: 22px; color: var(--silver-light);
    display: inline-block; padding: 0 40px 4px 0;
    border-bottom: 3px solid var(--silver-dim);
    margin-bottom: 8px;
  }
  .services__list {
    list-style: none;
    font-size: 19px; line-height: 1.42;
  }
  .services__list li { position: relative; padding-left: 30px; }
  .services__list li::before {
    content: ""; position: absolute; left: 6px; top: 10px;
    width: 7px; height: 7px; border-radius: 50%;
    background: var(--silver);
  }
</style>
</head>
<body>
<main class="sheet">
  <section class="card card--front" aria-label="Business card front">
    <div class="stripe-accent" role="img" aria-label="Soft silver vertical sheen accent"></div>
    <div class="brand-name">K&amp;T</div>
    <div class="contact-person">
      <p class="contact-person__name">Lewis Vintelli</p>
      <p class="contact-person__phone">046 720 5184</p>
    </div>
    <h1 class="business-title">K&amp;T HOME MAINTENANCE SERVICES</h1>
    <div class="business-details">
      <p>kntmaintenance@postvale.com</p>
      <p>ABN : 5714 032 8619</p>
    </div>
  </section>

  <section class="card card--back" aria-label="Business card back">
    <div class="stripe-accent" role="img" aria-label="Soft silver vertical sheen accent"></div>
    <div class="services">
      <h2 class="services__heading">Our services</h2>
      <ul class="services__list">
        <li>General household repairs and maintenance</li>
        <li>Painting</li>
        <li>Verolin/Plaster Repairs</li>
        <li>Fencing</li>
        <li>Gardening and landscaping</li>
        <li>Cleaning and removals</li>
        <li>Doors and windows</li>
        <li>Hinges and Locks</li>
        <li>Fly screen/ screen door Repairs</li>
      </ul>
    </div>
  </section>
</main>
</body>
</html>
```